Handmade candle business in melbourne requiring assistance with designing classy labels

My business name is Wick and Willow.
I specialise in making handmade candles, i'm based in Melbourne.
My moto is "Delicately hand poured and infused by me...for you"
wickwillow@mailbox-demo.net
0487 913 072

I need some assistance with designing my labels for my glass candles
I really like earthy colours and nothing too bright, but I want it to look classy and elegant and something that stands out from other homemade candle businesses.
I have attached a sample of a design that appeals to me but open to suggestions.

```html
<!DOCTYPE html>
<html lang="en">
<head>
<meta charset="utf-8">
<title>Wick and Willow – Candle Label</title>
<link href="https://fonts.googleapis.com/css2?family=Lora:wght@400;500&display=swap" rel="stylesheet">
<style>
  :root {
    --page: #eef5dc;
    --floral-base: #f47c7c;
    --floral-deep: #ee6470;
    --floral-peach: rgba(250, 196, 170, 0.55);
    --floral-yellow: rgba(240, 214, 110, 0.45);
    --floral-mauve: rgba(190, 130, 160, 0.45);
    --band: #d6d2c0;
    --band-edge: #bf9558;
    --seal-edge: #e9f3d2;
    --seal-ring: #c3d2a4;
    --seal-center: #c9c9a2;
    --seal-outer: #8f8a74;
    --ink: #3a342d;
    --rule: #6b6455;
  }
  * { margin: 0; padding: 0; box-sizing: border-box; }
  html, body {
    width: 1200px; height: 1000px; overflow: hidden;
    background: var(--page);
  }
  .label {
    position: relative; width: 1200px; height: 1000px;
    background: var(--page);
  }
  .floral-field {
    position: absolute; left: 0; width: 1200px;
    background:
      radial-gradient(circle at 12% 30%, var(--floral-yellow), transparent 18%),
      radial-gradient(circle at 30% 65%, var(--floral-peach), transparent 20%),
      radial-gradient(circle at 42% 25%, var(--floral-mauve), transparent 16%),
      radial-gradient(circle at 60% 70%, var(--floral-yellow), transparent 18%),
      radial-gradient(circle at 75% 30%, var(--floral-peach), transparent 20%),
      radial-gradient(circle at 90% 65%, var(--floral-mauve), transparent 16%),
      radial-gradient(ellipse at 50% 50%, var(--floral-base), var(--floral-deep));
  }
  .floral-field--top { top: 38px; height: 300px; }
  .floral-field--bottom { top: 632px; height: 330px; }
  .name-band {
    position: absolute; left: 0; top: 338px; width: 1200px; height: 294px;
    background: var(--band);
    border-top: 18px solid var(--band-edge);
    border-bottom: 18px solid var(--band-edge);
    box-shadow: 0 4px 10px rgba(0,0,0,0.18), 0 -4px 10px rgba(0,0,0,0.12);
  }
  .seal {
    position: absolute; left: 370px; top: 260px; width: 440px; height: 440px;
  }
  .seal svg { position: absolute; inset: 0; }
  .seal-text {
    position: absolute; inset: 0;
    font-family: "Lora", Georgia, serif;
    color: var(--ink);
    text-align: center;
  }
  .brand-mark {
    position: absolute; left: 50%; top: 90px; transform: translateX(-50%);
    width: 30px; height: 30px; border-radius: 50%;
    background: var(--seal-edge);
  }
  .brand-name {
    position: absolute; left: 0; right: 0; top: 198px;
    font-size: 38px; font-weight: 400; line-height: 1;
  }
  .divider {
    position: absolute; left: 140px; top: 303px; width: 160px; height: 1px;
    background: var(--rule);
  }
  .contact {
    position: absolute; left: 0; right: 0; top: 320px;
    font-size: 17px; line-height: 28px; letter-spacing: 0.3px;
    list-style: none;
  }
</style>
</head>
<body>
  <main class="label">
    <div class="floral-field floral-field--top" role="img" aria-label="Coral pink floral pattern with yellow, peach and mauve flowers and leaves"></div>
    <div class="floral-field floral-field--bottom" role="img" aria-label="Coral pink floral pattern with yellow, peach and mauve flowers and leaves"></div>
    <div class="name-band"></div>

    <div class="seal">
      <svg width="440" height="440" viewBox="0 0 440 440" aria-hidden="true">
        <defs>
          <radialGradient id="seal-face" cx="50%" cy="50%" r="50%">
            <stop offset="0%" stop-color="var(--seal-center)"/>
            <stop offset="100%" stop-color="var(--seal-outer)"/>
          </radialGradient>
          <filter id="seal-shadow" x="-10%" y="-10%" width="120%" height="120%">
            <feDropShadow dx="0" dy="3" stdDeviation="5" flood-opacity="0.3"/>
          </filter>
        </defs>
        <g filter="url(#seal-shadow)">
          <circle cx="220" cy="220" r="205" fill="var(--seal-edge)"/>
          <circle cx="220" cy="220" r="205" fill="none" stroke="var(--seal-edge)" stroke-width="16" stroke-linecap="round" stroke-dasharray="0 17.89"/>
        </g>
        <circle cx="220" cy="220" r="192" fill="none" stroke="var(--seal-ring)" stroke-width="8"/>
        <circle cx="220" cy="220" r="186" fill="url(#seal-face)"/>
      </svg>
      <div class="seal-text">
        <span class="brand-mark" aria-hidden="true"></span>
        <h1 class="brand-name">Wick and Willow</h1>
        <span class="divider" aria-hidden="true"></span>
        <ul class="contact">
          <li>wickwillow@mailbox-demo.net</li>
          <li>0487 913 072</li>
        </ul>
      </div>
    </div>
  </main>
</body>
</html>
```